KRV

I just wrote a novel that I plan on marketing through my website. Please use my uploaded files to add on to your design... The name of the book is "Ashes beneath the orchard".

Industry/Entity Type

Marketing

Font styles to use
Serif
Sans Serif

Colors

Designer to choose colors to be used in the design.

```html
<!DOCTYPE html>
<html lang="en">
<head>
<meta charset="utf-8">
<title>Ashes Beneath the Orchard</title>
<link rel="stylesheet" href="https://fonts.googleapis.com/css2?family=Oswald:wght@400;500&family=Open+Sans:wght@400;600&display=swap">
<style>
:root{
  --navy:#221f78;
  --red:#e0232b;
  --white:#ffffff;
  --text:#555555;
  --muted:#777777;
  --link:#6b9bef;
}
*{margin:0;padding:0;box-sizing:border-box}
html,body{width:898px;height:1200px;overflow:hidden;background:var(--white)}
body{position:relative;font-family:"Open Sans",Arial,sans-serif;color:var(--text)}
.page{position:relative;width:898px;height:1200px}

.site-header{position:absolute;left:0;top:0;width:898px;height:44px;background:var(--navy)}
.site-title{position:absolute;left:40px;top:11px;font-family:"Oswald",sans-serif;font-weight:500;font-size:17px;color:var(--white);letter-spacing:.2px}
.main-nav{position:absolute;right:32px;top:0;display:flex;height:44px}
.main-nav a{display:block;padding:12px 13px 0;font-family:"Open Sans",sans-serif;font-size:15px;color:var(--white);text-decoration:none}
.main-nav a.active{background:var(--red);color:var(--navy);margin-top:4px;padding-top:8px}

.hero{position:absolute;left:0;top:44px;width:898px;height:411px;background:radial-gradient(ellipse at 45% 45%,#ef3a3f 0%,#e0242b 60%,#cf1d24 100%)}
.hero-arrow{position:absolute;top:168px}
.hero-arrow.prev{left:55px}
.hero-arrow.next{right:56px}
.hero-copy{position:absolute;left:117px;top:112px;color:var(--white)}
.hero-title{font-family:"Oswald",sans-serif;font-weight:400;font-size:72px;line-height:1;letter-spacing:1px}
.hero-subtitle{font-family:"Oswald",sans-serif;font-size:31px;margin-top:14px;line-height:1}
.hero-author{font-family:"Oswald",sans-serif;font-size:25px;letter-spacing:4px;margin-top:18px}
.book-cover{position:absolute;left:530px;top:34px;width:208px;height:344px;background:linear-gradient(160deg,#c9c2c8 0%,#6b5f66 45%,#2a2430 100%);box-shadow:6px 8px 14px rgba(0,0,0,.35);border-right:6px solid #ddd}

.buy-bar{position:absolute;left:0;top:455px;width:898px;height:45px;background:var(--navy);display:flex;align-items:center;padding-left:40px}
.buy-label{font-weight:600;font-size:16px;color:var(--white);margin-right:15px}
.retailer{height:22px;background:var(--white);border:2px solid #cfcfcf;display:flex;align-items:center;justify-content:center;font-size:11px;font-weight:600;color:#333;margin-right:16px}

.author-section{position:absolute;left:40px;top:500px;width:571px;height:262px}
.section-heading{font-size:17px;color:var(--red);font-weight:400;position:absolute;left:0;top:21px}
.author-photo{position:absolute;left:1px;top:54px;width:153px;height:182px;background:linear-gradient(135deg,#c7d4de 0%,#8ea1b2 55%,#3c4a5e 100%);border:1px solid #ddd}
.author-bio{position:absolute;left:170px;top:51px;width:404px;font-size:10.7px;line-height:16.2px}
.author-bio p{margin-bottom:5px}
.read-more{position:absolute;left:505px;top:216px;width:66px;height:22px;background:var(--red);color:var(--white);font-size:10.5px;display:flex;align-items:center;justify-content:center}

.mailing-box{position:absolute;left:635px;top:525px;width:223px;height:213px;background:var(--navy);padding:13px 16px;color:var(--white)}
.mailing-box h3{font-weight:600;font-size:16.5px}
.mailing-box .hint{font-size:12px;margin-top:1px}
.email-field{margin-top:9px;width:190px;height:24px;background:var(--white);font-size:9.5px;color:#888;padding-left:9px;display:flex;align-items:center}
.signup{margin-top:10px;width:55px;height:21px;background:var(--red);font-size:10px;display:flex;align-items:center;justify-content:center}
.find-online{font-size:17px;margin-top:10px;font-weight:600}
.profile{display:flex;margin-top:5px}
.profile-photo{width:44px;height:43px;background:linear-gradient(135deg,#c7d4de,#3c4a5e)}
.profile-info{margin-left:8px}
.profile-name{color:var(--link);font-size:13px}
.follow-row{display:flex;align-items:center;margin-top:4px;font-size:10px;color:#9a9ac0}
.follow-btn{background:#4c66a4;color:var(--white);font-size:9.5px;font-weight:600;padding:1px 6px;margin-right:8px}

.story-band{position:absolute;left:0;top:762px;width:898px;height:226px;background:var(--navy)}
.story-copy{position:absolute;left:42px;top:18px;width:552px;color:var(--white)}
.story-copy h2{font-weight:400;font-size:20.5px}
.story-tagline{font-size:13.5px;margin-top:12px}
.story-tagline em{color:var(--red);font-style:normal}
.story-copy p.body{font-size:10.6px;line-height:18px;margin-top:5px;text-align:justify}
.publisher-panel{position:absolute;left:635px;top:0;width:223px;height:226px;background:var(--white)}
.publisher-mark{position:absolute;left:5px;top:6px;width:214px;height:214px;border-radius:50%;background:#111;display:flex;align-items:center;justify-content:center;font-weight:600;font-size:44px;color:var(--white)}

.site-footer{position:absolute;left:0;top:988px;width:898px;height:170px}
.footer-col{position:absolute;top:20px}
.footer-col h4{font-weight:400;font-size:16.5px;color:var(--red);margin-bottom:9px}
.footer-col li{list-style:none;font-size:11px;color:var(--muted);line-height:21.3px}
.footer-col li.current{color:var(--navy)}
.contact-item{display:flex;font-size:11px;color:var(--muted);line-height:16px;margin-bottom:17px}
.contact-item svg{flex:none;margin-right:7px;margin-top:1px}
.card-list{display:flex;flex-direction:column;gap:8px;margin-top:3px}
.card{width:32px;height:19px;border-radius:2px}

.bottom-bar{position:absolute;left:0;top:1158px;width:898px;height:42px;background:var(--red);color:var(--white)}
.copyright{position:absolute;left:40px;top:13px;font-size:11px}
.social{position:absolute;right:40px;top:9px;display:flex;gap:4px}
.social span{width:22px;height:22px;background:var(--navy);display:block}
</style>
</head>
<body>
<div class="page">

  <header class="site-header">
    <div class="site-title">ASHES BENEATH THE ORCHARD</div>
    <nav class="main-nav">
      <a class="active">Home</a><a>Reviews</a><a>About</a><a>Blog</a><a>Contact</a><a>Links</a>
    </nav>
  </header>

  <section class="hero">
    <svg class="hero-arrow prev" width="20" height="74" viewBox="0 0 20 74"><polyline points="18,2 2,37 18,72" fill="none" stroke="#fff" stroke-width="2"/></svg>
    <svg class="hero-arrow next" width="20" height="74" viewBox="0 0 20 74"><polyline points="2,2 18,37 2,72" fill="none" stroke="#fff" stroke-width="2"/></svg>
    <div class="hero-copy">
      <div class="hero-title">ASHES</div>
      <div class="hero-subtitle">BENEATH THE ORCHARD</div>
      <div class="hero-author">ELIAS.M.THORNE</div>
    </div>
    <div class="book-cover" role="img" aria-label="Book cover of Ashes Beneath the Orchard"></div>
  </section>

  <div class="buy-bar">
    <span class="buy-label">Buy Now</span>
    <span class="retailer" style="width:72px">Pagehall</span>
    <span class="retailer" style="width:78px">Inkwell &amp; Co</span>
    <span class="retailer" style="width:65px">Shelfside</span>
    <span class="retailer" style="width:87px">Northbind</span>
    <span class="retailer" style="width:69px">Quirebay</span>
  </div>

  <section class="author-section">
    <h2 class="section-heading">MEET ELIAS.M. THORNE</h2>
    <div class="author-photo" role="img" aria-label="Portrait photo of the author"></div>
    <div class="author-bio">
      <p>Lorem ipsum dolor sit amet, consectetur adipiscing elit. Maecenas malesuada accusan odio et interdum. Donec non iaculis mauris, et commodo ante. Aliquam pulvinar nisi ut tortor vestibulum, sit amet gravida ante feugiat. Curabitur ornare, neque a elemeum egestas, purus tortor convallis nisi, at adipiscing justo mauris</p>
      <p>Fusce lacinia commodo dui, ac hendrerit dolor rutrum quis. In dolor massa, faucibus id augue ac, viverra dapibus sem. Nam ac posuere lectus, at molestie felis. Proin volutpat sit amet leo id lobortis. Vivamus vestibulum arcu ac porttitor condimentum.Proin arcu diam, dignissim nec cursus in, placerat eget dolor. Pellentesque non elit ac lacus sodales cursus. Vivamus volutpat feugiat mi id faucibus</p>
    </div>
    <div class="read-more">Read More</div>
  </section>

  <aside class="mailing-box">
    <h3>MAILING LIST</h3>
    <div class="hint">Sign up for email updates:</div>
    <div class="email-field">Enter your e-mail address</div>
    <div class="signup">SIGN UP</div>
    <div class="find-online">Find Elias Online</div>
    <div class="profile">
      <div class="profile-photo" role="img" aria-label="Small author profile photo"></div>
      <div class="profile-info">
        <div class="profile-name">Elias M.Thorne</div>
        <div class="follow-row"><span class="follow-btn">Follow</span>125 Peole like</div>
      </div>
    </div>
  </aside>

  <section class="story-band">
    <div class="story-copy">
      <h2>ASHES BENEATH THE ORCHARD</h2>
      <div class="story-tagline">A story Of <em>Moeny Murder, Sex and Family</em> ties in the hear of the city.</div>
      <p class="body">Read along as Elias M.Thorne Masterfully paint this wllimingation, Deaware tale tale like no other -The M.O.B. boys" clash in a rain bullets against north side own "yaho boys.<br>
      Lorem ipsum dolor sit amet, consectetur adipiscing elit. Etiam rhoncus lacus vel sapien rutr sit amet pellentesque ipsum imperdiet. Vestibulum a dignissim lacus. Donec ac euismod eros. Aenean pharetra lorem at suscipit malesuada.Donec adicing odio ac libero viverra, ut consequat diam hendrerit. Quisque intedum massa sit amet sem condiment aliquet eget in tortor. Duis odio urna, faucibus vel adipiscing quis, varius fermentum tellus. Quisque quis vestibulum nibhaecenas eu tempor magna. Aliquam at dapibus nisi.</p>
    </div>
    <div class="publisher-panel">
      <div class="publisher-mark">KRV</div>
    </div>
  </section>

  <footer class="site-footer">
    <div class="footer-col" style="left:40px">
      <h4>The Website</h4>
      <ul><li class="current">Home Page</li><li>Contact Information</li><li>Elias Thorne Biography</li><li>Interview with Elias Thorne</li><li>Frequently Asked Questions</li></ul>
    </div>
    <div class="footer-col" style="left:272px">
      <h4>The News</h4>
      <ul><li>Novel</li><li>Recent News</li><li>Elias Thorne Blog</li><li>Follow Elias on Chirp</li><li>Upcoming Events</li></ul>
    </div>
    <div class="footer-col" style="left:461px">
      <h4>Contact</h4>
      <div class="contact-item">
        <svg width="18" height="16" viewBox="0 0 18 16"><path d="M9 1a4 4 0 0 0-4 4c0 3 4 7 4 7s4-4 4-7a4 4 0 0 0-4-4z" fill="none" stroke="#221f78" stroke-width="1.4"/><circle cx="9" cy="5" r="1.4" fill="#221f78"/><path d="M1 15l3-4h10l3 4z" fill="none" stroke="#221f78" stroke-width="1.2"/></svg>
        <span>Elias Thorne PO Box 20417<br>Harlow Bay</span>
      </div>
      <div class="contact-item">
        <svg width="18" height="16" viewBox="0 0 18 16"><path d="M6 1c-2 1-3 3-3 7s1 6 3 7l1-4-2-3 2-3z" fill="#221f78"/></svg>
        <span>Phone: +302 555 0148</span>
      </div>
      <div class="contact-item">
        <svg width="18" height="16" viewBox="0 0 18 16"><rect x="2" y="3" width="13" height="9" fill="none" stroke="#221f78" stroke-width="1.2"/><polyline points="2,3 8.5,8.5 15,3" fill="none" stroke="#221f78" stroke-width="1.2"/></svg>
        <span>Email: ashesorchard@mailbox.test</span>
      </div>
    </div>
    <div class="footer-col" style="left:788px">
      <h4>Payment</h4>
      <div class="card-list">
        <span class="card" style="background:#2b7cc4" role="img" aria-label="Cardline"></span>
        <span class="card" style="background:#2a3f8f" role="img" aria-label="Paywell"></span>
        <span class="card" style="background:#e9e4df" role="img" aria-label="Tallypay"></span>
        <span class="card" style="background:#e86a2a" role="img" aria-label="Coinrow"></span>
      </div>
    </div>
  </footer>

  <div class="bottom-bar">
    <div class="copyright">Copyright © 2014 ashesbeneaththeorchard . All Rights Reserved.</div>
    <div class="social">
      <span role="img" aria-label="Folio"></span><span role="img" aria-label="Chirp"></span><span role="img" aria-label="Circlet"></span><span role="img" aria-label="Pinbook"></span><span role="img" aria-label="Reelcast"></span><span role="img" aria-label="News feed"></span><span role="img" aria-label="Worknet"></span>
    </div>
  </div>

</div>
</body>
</html>
```